BVSU, Bureau of Digital Services responsive website

We need a responsive web design for BVSU's Bureau of Digital Services, see https://bds.bvsu-example.edu/ that will look good on all three platforms, PC Web browser, tablet & phone. Please use http://www.bvsu-example.edu as and indication of design genre. A full design will show off all three versions of what the wide screen, tablet and phone will look like,using good responsive design concepts. Minimal text embedded in images for good accessibility. An acceptable design must meet WCAG 2.0 standards for color contrast and beyond. Please note, that much more work could come to good designers, if this works out!
KEY concepts: Cultured, Visionary, Perseverance, catalytic
For the 4 pages, I want to see the home page, the tablet view, the mobile view and also a sub theme page

Target Market(s)

Faculty, Staff, Students, Technologists

Industry/Entity Type

Information Technology

Coding

Coded - Design and coding required

Number of Pages Required

Font styles to use
Serif
Sans Serif
Other font styles liked:
• Karbon

Colors
0492cd
3176b5
fbed22
ffc214
fbee3e

Requirements
Must have
• My project must use the existing BDS logo on the current website: http://bds.bvsu-example.edu, it must look good with responsive design, thus in all sizes, for a PC, on a tablet on and a mobile phone.
• It must have a way to feature events and content, it must feature the current homepage content, but have a new navigation plan that works well with responsive design. An acceptable design must meet WCAG 2.0 standards for color contrast and beyond. It must have a menu that reduces down to an icon on a mobile phone, it must not find a way to get content to stack vertically
Nice to have
• It would be nice to see their be continuity between the PC, TAblet and mobile phone design, it would be nice to see elements of http://www.bvsu-example.edu embedded into the design
Should not have
• text embedded in the logo, a design that is not conducive to responsive design, it must not use ANY tables

```html
<!DOCTYPE html>
<html lang="en">
<head>
<meta charset="utf-8">
<title>BVSU Bureau of Digital Services</title>
<link href="https://fonts.googleapis.com/css2?family=Open+Sans:wght@400;600;700&display=swap" rel="stylesheet">
<style>
:root{
  --nav:#1b7fc4;
  --nav-active:#16609f;
  --about:#1b86cf;
  --yellow:#fbed22;
  --gold:#ffc214;
  --icon:#1d5fa6;
  --title:#1f5ea8;
  --panel:#efefef;
  --ink:#3b3b3b;
  --card:#262626;
  --footer:#1c6db5;
}
*{box-sizing:border-box;margin:0;padding:0}
html,body{width:776px;height:1200px;overflow:hidden}
body{font-family:"Open Sans",Arial,sans-serif;background:#fff;position:relative;color:var(--ink)}
.topnav{position:absolute;left:0;top:0;width:776px;height:27px;background:var(--nav)}
.topnav ul{list-style:none;display:flex;position:absolute;left:64px;top:0;height:27px}
.topnav li{height:27px;display:flex;align-items:center;justify-content:center;color:#fff;font-size:8.5px;border-right:1px solid rgba(255,255,255,.18)}
.topnav li.active{background:var(--nav-active)}
.header{position:absolute;left:0;top:27px;width:776px;height:68px}
.brand{position:absolute;left:64px;top:16px;display:flex;align-items:center;gap:6px;color:#222;font-weight:600}
.brand .dot{width:12px;height:12px;border-radius:50%;background:var(--nav)}
.brand .mark{font-size:24px;line-height:1}
.brand .full{font-size:8px;line-height:1.3}
.social{position:absolute;left:454px;top:30px;display:flex;gap:4.5px}
.social span{width:18px;height:18px;border-radius:50%}
.search{position:absolute;left:594px;top:27px;width:117px;height:22px;border:1px solid #ccc;font-size:7px;color:#aaa;padding:6px 8px}
.search svg{position:absolute;right:6px;top:5px}
.hero{position:absolute;left:0;top:95px;width:776px;height:283px;background:linear-gradient(100deg,#1d232b 0%,#3a4651 45%,#56606a 65%,#1b1f24 100%)}
.hero-text{position:absolute;left:64px;top:89px;width:216px;height:106px;background:rgba(20,20,20,.55);padding:10px 12px}
.hero-text h2{color:var(--gold);font-size:13px;font-weight:600;line-height:1.38;text-transform:uppercase}
.btn{display:inline-block;margin-top:7px;background:var(--gold);color:#222;font-size:8px;padding:5px 7px;border-radius:2px}
.arrow{position:absolute;top:133px}
.about{position:absolute;left:64px;top:404px;width:648px;height:99px;background:var(--about);text-align:center;color:#fff}
.about h2{color:var(--yellow);font-size:16px;font-weight:700;margin-top:18px}
.about p{font-size:8.6px;line-height:1.55;width:470px;margin:5px auto 0}
.whatwedo{position:absolute;left:64px;top:503px;width:648px;height:211px;background:var(--panel)}
.whatwedo h2{position:absolute;top:24px;width:100%;text-align:center;color:var(--title);font-size:17px;font-weight:700}
.service{position:absolute;top:65px;width:110px;text-align:center}
.service .circle{width:62px;height:62px;border-radius:50%;background:var(--icon);margin:0 auto;display:flex;align-items:center;justify-content:center}
.service h3{color:var(--title);font-size:8.6px;font-weight:700;margin-top:8px;line-height:1.2}
.service p{font-size:6.8px;line-height:1.45;color:#444;margin-top:3px}
.people{position:absolute;left:0;top:736px;width:776px;text-align:center}
.people h2{font-size:17px;font-weight:700;color:#3b3b3b}
.people p{font-size:8.4px;color:#555;margin-top:4px}
.people a{color:var(--title);text-decoration:none}
.card{position:absolute;top:785px;width:322px;height:84px;background:var(--card);color:#fff}
.card .photo{position:absolute;left:0;top:0;width:102px;height:84px}
.card .body{position:absolute;left:117px;top:10px;width:196px}
.card h3{font-size:9.5px;font-weight:700}
.card p{font-size:7px;line-height:1.45;color:#ddd;margin-top:6px}
.card time{display:block;font-size:6.8px;color:#aaa;margin-top:4px}
.links{position:absolute;top:902px;height:208px;background:var(--panel);padding:9px 5px 0 13px}
.links h3{font-size:13.5px;font-weight:700;color:#8a8a8a;line-height:1.15;text-transform:uppercase;height:37px}
.links ul{list-style:none;border-top:1px solid #ddd;margin-top:4px}
.links li{font-size:7.8px;color:#555;padding:5.5px 0 5.5px 7px;border-bottom:1px solid #ddd;position:relative;line-height:1.25}
.links li::before{content:"";position:absolute;left:0;top:9.5px;width:2px;height:2px;background:#777}
.footer{position:absolute;left:0;top:1110px;width:776px;height:90px;background:var(--footer);color:#fff}
.footer ul{list-style:none;display:flex;justify-content:center;gap:19px;margin-top:19px;font-size:6.8px}
.footer ul li:first-child{font-weight:700}
.footer hr{border:0;border-top:1px solid rgba(255,255,255,.3);width:648px;margin:13px auto 0}
.footer small{display:block;text-align:center;font-size:7px;margin-top:13px}
</style>
</head>
<body>
<nav class="topnav"><ul>
  <li class="active" style="width:92px">HOME</li>
  <li style="width:106px">MISSION</li>
  <li style="width:119px">INITIATIVES</li>
  <li style="width:126px">GOVERNANCE</li>
  <li style="width:110px">SERVICES</li>
  <li style="width:95px">ABOUT</li>
</ul></nav>

<header class="header">
  <div class="brand"><span class="dot"></span><span class="mark">BDS</span><span class="full">BUREAU OF DIGITAL SERVICES<br>BVSU</span></div>
  <div class="social">
    <span style="background:#3b5998"></span><span style="background:#1da1f2"></span><span style="background:#333"></span>
    <span style="background:#f57d00"></span><span style="background:#e52d27"></span><span style="background:#5aa63a"></span>
  </div>
  <div class="search">SEARCH
    <svg width="10" height="10" viewBox="0 0 10 10"><circle cx="4" cy="4" r="3" fill="none" stroke="#1b7fc4" stroke-width="1.5"/><line x1="6.2" y1="6.2" x2="9" y2="9" stroke="#1b7fc4" stroke-width="1.5"/></svg>
  </div>
</header>

<section class="hero" role="img" aria-label="Photo of a team gathered around a desk reviewing documents">
  <svg class="arrow" style="left:17px" width="10" height="16" viewBox="0 0 10 16"><polyline points="8,1 2,8 8,15" fill="none" stroke="#aaa" stroke-width="1.6"/></svg>
  <svg class="arrow" style="left:748px" width="10" height="16" viewBox="0 0 10 16"><polyline points="2,1 8,8 2,15" fill="none" stroke="#aaa" stroke-width="1.6"/></svg>
  <div class="hero-text">
    <h2>Dana Whitlow and Marisol Kerrigan lead new data governance task force</h2>
    <span class="btn">Read more</span>
  </div>
</section>

<section class="about">
  <h2>ABOUT US</h2>
  <p>BDS seeks to strengthen BVSU's data cyberinfrastructure; provide research, education and mobility platforms that offer shared tools and collaboration resources; and establish the internal and external communities to build policies, practices and rich sharing of expertise and applications.</p>
</section>

<section class="whatwedo">
  <h2>WHAT WE DO</h2>
  <div class="service" style="left:11px">
    <div class="circle"><svg width="22" height="22" viewBox="0 0 22 22"><path d="M10 3a8 8 0 1 0 8 9h-8z" fill="#fff"/><path d="M12 1v9h9a9 9 0 0 0-9-9z" fill="#fff"/></svg></div>
    <h3>INITIATIVES</h3><p>Digital Research &amp; Education, Educational Technology, Digital Citizenship</p>
  </div>
  <div class="service" style="left:141px">
    <div class="circle"><svg width="20" height="24" viewBox="0 0 20 24"><path d="M2 1h11l5 5v17H2z" fill="none" stroke="#fff" stroke-width="1.8"/><path d="M6 10h8M6 14h8M6 18h8" stroke="#fff" stroke-width="1.5"/></svg></div>
    <h3>STRATEGY, GOVER-<br>NANCE &amp; POLICY</h3><p>IT Governance, Data Security, Privacy, Accessibility</p>
  </div>
  <div class="service" style="left:272px">
    <div class="circle"><svg width="26" height="22" viewBox="0 0 26 22"><circle cx="9" cy="12" r="6" fill="none" stroke="#fff" stroke-width="3.5" stroke-dasharray="2.4 1.6"/><circle cx="9" cy="12" r="2" fill="#fff"/><circle cx="20" cy="6" r="3.5" fill="none" stroke="#fff" stroke-width="2.5" stroke-dasharray="1.6 1.2"/><circle cx="20" cy="17" r="3" fill="none" stroke="#fff" stroke-width="2.2" stroke-dasharray="1.4 1.1"/></svg></div>
    <h3>RESOURCES &amp; SERVICES</h3><p>Computational research, Software discounts, Consult-ing, Facilities</p>
  </div>
  <div class="service" style="left:403px">
    <div class="circle"><svg width="26" height="22" viewBox="0 0 26 22"><circle cx="13" cy="6" r="4" fill="#fff"/><circle cx="5" cy="8" r="3" fill="#fff"/><circle cx="21" cy="8" r="3" fill="#fff"/><path d="M6 21v-5a7 6 0 0 1 14 0v5z" fill="#fff"/><path d="M0 19v-3a5 4 0 0 1 7-3v6zM26 19v-3a5 4 0 0 0-7-3v6z" fill="#fff"/></svg></div>
    <h3>INDUSTRY<br>PARTNERSHIPS</h3><p>Tech Associates, Smart Manufacturing, Educational Advisory Board</p>
  </div>
  <div class="service" style="left:534px">
    <div class="circle"><svg width="26" height="22" viewBox="0 0 26 22"><rect x="1" y="1" width="24" height="15" fill="none" stroke="#fff" stroke-width="2"/><path d="M10 16h6v3h3v2H7v-2h3z" fill="#fff"/></svg></div>
    <h3>OUTREACH &amp;<br>LEARNING</h3><p>Conferences, Online training, Symposiums</p>
  </div>
</section>

<section class="people">
  <h2>PEOPLE &amp; PROGRAMS</h2>
  <p>Get the latest information about BDS, research at BVSU and the national research community. Check out the <a href="#">News</a> and <a href="#">Events</a>.</p>
</section>

<article class="card" style="left:64px">
  <div class="photo" role="img" aria-label="Photo of two staff members standing outdoors" style="background:linear-gradient(160deg,#5d7a3e,#6b5f8a 70%,#8c7a63)"></div>
  <div class="body"><h3>PEOPLE</h3><p>Phasellus nisl est, condimentum vitae faucibus in, sollici tudin vel metus. Sed libero felis, vestibulum et dolor eget, lacinia aliquet neque.</p><time>Apr 09, 2015</time></div>
</article>
<article class="card" style="left:390px">
  <div class="photo" role="img" aria-label="Photo of program participants seated in a vehicle" style="background:linear-gradient(160deg,#9aa3ad,#4a5a78 60%,#d8dde3)"></div>
  <div class="body"><h3>PROGRAMS</h3><p>Phasellus nisl est, condimentum vitae faucibus in, sollici tudin vel metus. Sed libero felis, vestibulum et dolor eget, lacinia aliquet neque.</p><time>Apr 09, 2015</time></div>
</article>

<section class="links" style="left:64px;width:158px">
  <h3>Organizational Structure</h3>
  <ul><li>Community Partnership Programs</li><li>Educational Technology Systems &amp; Administration</li><li>IRCE</li><li>Mobile and Web Strategy, Education &amp; Research</li><li>Operations and Finance</li><li>Policy</li></ul>
</section>
<section class="links" style="left:226px;width:158px">
  <h3>Software and Services</h3>
  <ul><li>Accessibility Consulting</li><li>Accessible Computing Program</li><li>Mobile Web Framework</li><li>Software Hub</li><li>Software Development</li><li>Web Consulting</li><li>Meeting/Presentation Facilities</li></ul>
</section>
<section class="links" style="left:389px;width:157px">
  <h3>Research and Learning</h3>
  <ul><li>Cloud Storage</li><li>MediaCast U</li><li>FieldMobile Labs Initiative</li><li>Research Informatics</li></ul>
</section>
<section class="links" style="left:550px;width:162px">
  <h3>Community and Governance</h3>
  <ul><li>TechForum</li><li>Governance</li><li>Tech Associates</li><li>IT Horizon Strategic Plan</li><li>Privacy</li></ul>
</section>

<footer class="footer">
  <ul><li>HOME</li><li>MISSION</li><li>INITIATIVES</li><li>GOVERNANCE</li><li>SERVICES</li><li>ABOUT</li></ul>
  <hr>
  <small>Copyright © 2015 BDS-BVSU. All rights reserved.</small>
</footer>
</body>
</html>
```